Slide desk development crimson ledge holdings

I am looking to expand the range of slide templates we have using our new branded powerpoint deck so the team have more options.

Target Market(s)

We operate in the construction sector

Industry/Entity Type

Construction

Requirements
Must have
• Picture linking back to construction

```html
<!DOCTYPE html>
<html lang="en">
<head>
<meta charset="utf-8">
<title>Crimson Ledge Holdings – Slide Deck Templates</title>
<link href="https://fonts.googleapis.com/css2?family=Lexend:wght@300;400;600;700;800&display=swap" rel="stylesheet">
<style>
  :root{
    --board:#8e8a8a;
    --ink:#000000;
    --panel:#0b0b0b;
    --panel-soft:#161616;
    --line:#2e2e2e;
    --white:#ffffff;
    --muted:#bdbdbd;
    --green:#62cf36;
    --green-light:#95ea62;
    --green-deep:#3fae20;
  }
  *{box-sizing:border-box;margin:0;padding:0}
  html,body{width:1102px;height:1200px;overflow:hidden}
  body{background:var(--board);font-family:"Lexend",sans-serif;color:var(--white);position:relative}

  .slide{position:absolute;width:750px;height:422px;transform:scale(.5965);transform-origin:0 0;overflow:hidden;background:var(--ink)}
  .col-left{left:97px}.col-right{left:559px}
  .row-1{top:79px}.row-2{top:342px}.row-3{top:605px}.row-4{top:868px}
  .abs{position:absolute}
  .shapes{position:absolute;inset:0;width:750px;height:422px}

  .slide-title{position:absolute;left:57px;top:60px;font-weight:700;font-size:20px;letter-spacing:.2px}

  .brand{display:flex;align-items:center;gap:10px;position:absolute;font-weight:400;color:var(--white);white-space:nowrap}
  .brand-mark{background:var(--green);flex:none}
  .brand-footer{left:35px;top:372px;font-size:14px}
  .brand-footer .brand-mark{width:14px;height:14px}
  .brand-hero{font-size:30px;gap:14px}
  .brand-hero .brand-mark{width:30px;height:30px}

  .page-no{position:absolute;left:722px;top:392px;width:18px;height:20px;background:var(--green);
    clip-path:polygon(50% 0,100% 25%,100% 75%,50% 100%,0 75%,0 25%);
    font-size:6.5px;color:#0a0a0a;display:flex;align-items:center;justify-content:center;font-weight:400}

  .photo{position:absolute}

  /* Title slide */
  .cover-bg{position:absolute;inset:0;background:radial-gradient(ellipse at 50% 45%,#4a4a4a 0%,#2c2c2c 45%,#141414 100%)}
  .cover .brand-hero{left:50%;top:136px;transform:translateX(-50%)}
  .cover-heading{position:absolute;left:0;right:0;top:248px;text-align:center;font-weight:700;font-size:31px;line-height:42px}
  .cover-date{position:absolute;left:0;right:0;top:352px;text-align:center;font-weight:300;font-size:17px}

  /* Agenda */
  .agenda-list{position:absolute;left:57px;top:116px;width:370px;list-style:none}
  .agenda-list li{display:flex;align-items:center;height:42px;font-weight:300;font-size:12.5px}
  .agenda-list .label{width:199px}
  .agenda-list .rule{width:135px;height:1px;background:#555;margin-top:6px}
  .agenda-list .num{margin-left:18px;margin-top:12px;font-size:11.5px}

  /* About */
  .about-lead{position:absolute;left:57px;top:104px;width:300px;color:var(--green);font-weight:700;font-size:14.5px;line-height:18px}
  .about-copy{position:absolute;left:57px;top:172px;width:285px;font-weight:300;font-size:11.5px;line-height:21.6px;text-align:justify}

  /* Section divider */
  .divider-bg{position:absolute;inset:0;background:radial-gradient(ellipse at 18% 40%,#3a3a3a 0%,#1b1b1b 40%,#050505 75%)}
  .divider .brand-hero{left:308px;top:162px}
  .divider-heading{position:absolute;left:306px;top:252px;font-weight:800;font-size:38px;white-space:nowrap}

  /* How it works */
  .works-bg{position:absolute;inset:0;background:radial-gradient(ellipse at 70% 80%,#1d1d1d 0%,#0a0a0a 60%)}
  .step{position:absolute;text-align:center}
  .step-label{color:var(--green-light);font-size:8.5px;font-weight:400;margin-bottom:27px}
  .step-copy{font-weight:300;font-size:7.4px;line-height:13.5px;color:#e6e6e6}

  /* Graph */
  .graph-copy{position:absolute;left:57px;top:106px;width:238px;font-weight:300;font-size:10px;line-height:19.6px;text-align:justify}
  .chart-box{position:absolute;left:341px;top:71px;width:328px;height:295px;border-radius:10px;background:#040404;border:1px solid #262626}

  /* Table */
  .table-intro{position:absolute;left:211px;top:53px;width:420px;font-weight:300;font-size:9.4px;line-height:19.5px}
  .data-table{position:absolute;left:60px;top:126px;width:629px;border-collapse:separate;border-spacing:0 2px;font-size:8px}
  .data-table th{background:var(--green);height:33px;font-weight:400;font-size:10px;color:#111;text-align:center}
  .data-table th:first-child{border-radius:7px 0 0 7px}
  .data-table th:last-child{border-radius:0 7px 7px 0;text-align:left;padding-left:30px}
  .data-table td{height:31px;border-top:1px solid var(--line);border-bottom:1px solid var(--line);background:#060606;text-align:center;font-weight:300}
  .data-table td+td{border-left:1px solid var(--line)}
  .data-table td:first-child{border-left:1px solid var(--line);border-radius:6px 0 0 6px;font-weight:400;font-size:7.5px}
  .data-table td:last-child{border-right:1px solid var(--line);border-radius:0 6px 6px 0;text-align:left;padding-left:30px;font-size:7.2px;line-height:11px}
  .data-table .status{color:var(--green-light)}

  /* Thank you */
  .thanks-bg{position:absolute;inset:0;background:linear-gradient(160deg,#2a2a2a 0%,#121212 50%,#1e1e1e 100%)}
  .thanks .brand-hero{left:50%;top:122px;transform:translateX(-50%)}
  .thanks-rule{position:absolute;left:170px;top:230px;width:410px;height:3px;background:var(--green)}
  .thanks-heading{position:absolute;left:0;right:0;top:258px;text-align:center;font-weight:800;font-size:62px;letter-spacing:1px}
</style>
</head>
<body>

<!-- Cover -->
<section class="slide cover col-left row-1">
  <div class="cover-bg" role="img" aria-label="Dark monochrome photo of two business people shaking hands over a construction plan"></div>
  <div class="brand brand-hero"><span class="brand-mark"></span>Crimson Ledge Holdings</div>
  <h1 class="cover-heading">Driving Construction<br>Labour Management Standard</h1>
  <p class="cover-date">November 01,2025</p>
</section>

<!-- How it works -->
<section class="slide works col-right row-1">
  <div class="works-bg"></div>
  <svg class="shapes" viewBox="0 0 750 422">
    <defs>
      <linearGradient id="cornerGreen" x1="0" y1="0" x2="1" y2="1">
        <stop offset="0" stop-color="#3fae20"/><stop offset="1" stop-color="#8ee65a"/>
      </linearGradient>
    </defs>
    <polygon points="592,0 750,0 750,129" fill="url(#cornerGreen)"/>
    <path d="M10,218 H58 Q68,218 68,208 V152 Q68,142 78,142 H240 Q250,142 250,152 V283 Q250,293 260,293 H420 Q430,293 430,283 V152 Q430,142 440,142 H599 Q609,142 609,152 V208 Q609,218 619,218 H668"
          fill="none" stroke="#6b6b6b" stroke-width="1.5"/>
    <circle cx="10" cy="218" r="8" fill="#7bd94b" stroke="#2f6a19" stroke-width="2"/>
    <circle cx="161" cy="142" r="5" fill="#7bd94b" stroke="#2f6a19" stroke-width="2"/>
    <circle cx="340" cy="293" r="5" fill="#7bd94b" stroke="#2f6a19" stroke-width="2"/>
    <circle cx="519" cy="142" r="5" fill="#7bd94b" stroke="#2f6a19" stroke-width="2"/>
    <circle cx="669" cy="219" r="8" fill="#7bd94b" stroke="#2f6a19" stroke-width="2"/>
  </svg>
  <h2 class="slide-title">How It Works</h2>

  <div class="step" style="left:99px;top:113px;width:126px">
    <p class="step-label">Protect your business</p>
    <p class="step-copy">We identify risk to enable risk mitigation helping our clients maintain compliant supply chains free of high risk practices.</p>
  </div>
  <div class="step" style="left:268px;top:265px;width:145px">
    <p class="step-label">Satisfy stakeholders</p>
    <p class="step-copy">We provide confidence to internal and external stakeholders that your business has a robust toolkit for building a more resilient and socially responsible supply chain.</p>
  </div>
  <div class="step" style="left:458px;top:113px;width:122px">
    <p class="step-label">Drive Improvement</p>
    <p class="step-copy">Our approach is designed to drive improvement through the supply chain by driving all suppliers to understand more about the companies that help deliver their offering and the practices they adopt to protect and develop the workforce.</p>
  </div>
  <div class="step" style="left:610px;top:241px;width:136px">
    <p class="step-label" style="margin-bottom:6px">Reduce Labour Related Issue</p>
    <p class="step-copy">By driving improvement and fostering the best working conditions. We reduce risk by increasing compliance. We reduce cost by reducing workforce churn and increasing productivity. We reduce skills shortages by ensuring better labour practices.</p>
  </div>

  <div class="brand brand-footer"><span class="brand-mark"></span>Crimson Ledge Holdings</div>
  <div class="page-no">05</div>
</section>

<!-- Agenda -->
<section class="slide agenda col-left row-2">
  <svg class="shapes" viewBox="0 0 750 422">
    <defs>
      <linearGradient id="bandGreenA" x1="0" y1="1" x2="1" y2="0">
        <stop offset="0" stop-color="#4cc22a"/><stop offset="1" stop-color="#a4ee74"/>
      </linearGradient>
    </defs>
    <polygon points="711,80 750,32 750,300 711,348" fill="url(#bandGreenA)"/>
    <polygon points="430,422 481,361 722,361 672,422" fill="url(#bandGreenA)"/>
    <rect x="481" y="38" width="228" height="345" fill="#050505"/>
  </svg>
  <h2 class="slide-title">Our Agenda</h2>
  <ul class="agenda-list">
    <li><span class="label">Introduction</span><span class="rule"></span><span class="num">02</span></li>
    <li><span class="label">Accreditation</span><span class="rule"></span><span class="num">03</span></li>
    <li><span class="label">Academy</span><span class="rule"></span><span class="num">04</span></li>
    <li><span class="label">Specialist Audit &amp; Compliance</span><span class="rule"></span><span class="num">05</span></li>
    <li><span class="label">Contact</span><span class="rule"></span><span class="num">06</span></li>
  </ul>
  <div class="photo" style="left:490px;top:46px;width:211px;height:330px;background:linear-gradient(180deg,#c9ccd0 0%,#8b8f94 30%,#d9672c 62%,#8a8f96 100%)"
       role="img" aria-label="Photo of a smiling construction worker in a white hard hat and orange hi-vis vest on site"></div>
  <div class="brand brand-footer"><span class="brand-mark"></span>Crimson Ledge Holdings</div>
  <div class="page-no">02</div>
</section>

<!-- Graph -->
<section class="slide graph col-right row-2">
  <div class="works-bg"></div>
  <svg class="shapes" viewBox="0 0 750 422">
    <polygon points="592,0 750,0 750,129" fill="url(#cornerGreen)"/>
  </svg>
  <h2 class="slide-title">Our Graph</h2>
  <p class="graph-copy">At vero eos et accusamus et iusto odio dignissimducimus qui blanditiis praesentiuluptatum deleniti atque corrupti qus molestias excepturi sint occaecati cupiditate non provident, similique sunt in culpa qui officia deserunt mollitia animi, id est laborum et dolorum fugvero eos et accusamus et iusto odio dignissimos ducimus qui blanditiis praesentium voluptatum deleniti atque corrupti quos dolores et quas molestias excepturi sint occaecati cupiditate non providentsimilique sunt in culpa qui officia deseruntum et dolorum fuga.</p>
  <div class="chart-box"></div>
  <svg class="shapes" viewBox="0 0 750 422" font-family="Lexend, sans-serif">
    <text x="504" y="102" fill="#fff" font-size="10.5" text-anchor="middle">Chart Title</text>
    <g stroke="#3a3a3a" stroke-width="1">
      <line x1="374" x2="646" y1="116" y2="116"/><line x1="374" x2="646" y1="143" y2="143"/>
      <line x1="374" x2="646" y1="170" y2="170"/><line x1="374" x2="646" y1="197" y2="197"/>
      <line x1="374" x2="646" y1="225" y2="225"/><line x1="374" x2="646" y1="252" y2="252"/>
      <line x1="374" x2="646" y1="279" y2="279"/><line x1="374" x2="646" y1="306" y2="306" stroke="#666"/>
    </g>
    <g fill="#ddd" font-size="7.5" text-anchor="end">
      <text x="366" y="119">14</text><text x="366" y="146">12</text><text x="366" y="173">10</text>
      <text x="366" y="200">8</text><text x="366" y="228">6</text><text x="366" y="255">4</text>
      <text x="366" y="282">2</text><text x="366" y="309">0</text>
    </g>
    <polyline points="402,248 456,272 510,257 564,245 617,306" fill="none" stroke="#3c3c3c" stroke-width="1.6"/>
    <polyline points="402,215 456,212 510,233 564,207 617,306" fill="none" stroke="#ffffff" stroke-width="1.6"/>
    <polyline points="402,188 456,185 510,193 564,139 617,306" fill="none" stroke="#6ad23d" stroke-width="1.6"/>
    <g fill="#ddd" font-size="7.5" text-anchor="middle">
      <text x="402" y="319">Category 1</text><text x="456" y="319">Category 2</text>
      <text x="510" y="319">Category 3</text><text x="564" y="319">Category 4</text>
    </g>
    <g font-size="7" fill="#ddd">
      <line x1="427" x2="441" y1="333" y2="333" stroke="#555" stroke-width="1.6"/><text x="444" y="336">Series 1</text>
      <line x1="482" x2="496" y1="333" y2="333" stroke="#fff" stroke-width="1.6"/><text x="499" y="336">Series 2</text>
      <line x1="537" x2="551" y1="333" y2="333" stroke="#6ad23d" stroke-width="1.6"/><text x="554" y="336">Series 3</text>
    </g>
  </svg>
  <div class="brand brand-footer"><span class="brand-mark"></span>Crimson Ledge Holdings</div>
  <div class="page-no">06</div>
</section>

<!-- About -->
<section class="slide about col-left row-3">
  <svg class="shapes" viewBox="0 0 750 422">
    <defs>
      <linearGradient id="bandGreenB" x1="0" y1="1" x2="1" y2="0">
        <stop offset="0" stop-color="#4cc22a"/><stop offset="1" stop-color="#b1f285"/>
      </linearGradient>
    </defs>
    <polygon points="672,160 750,30 750,245 672,368" fill="url(#bandGreenB)"/>
    <polygon points="430,422 486,368 702,368 650,422" fill="url(#bandGreenB)"/>
  </svg>
  <h2 class="slide-title">About Us</h2>
  <p class="about-lead">Why work with Crimson Ledge Holdings when managing your supply chain</p>
  <p class="about-copy">We are a boutique consultancy delivering purpose driven solutions with a shared value proposition that specialises in employment and temporary labour practices across the built environment. Our mantra is to challenge, educate and innovate helping our clients deliver market leading ethical labour strategies that drive improvement.</p>
  <div class="photo" style="left:399px;top:56px;width:273px;height:312px;background:linear-gradient(135deg,#d9cf6a 0%,#b8894f 35%,#e0702c 65%,#2b3646 100%)"
       role="img" aria-label="Photo of two smiling construction workers in yellow and orange hard hats with hi-vis vests"></div>
  <div class="brand brand-footer"><span class="brand-mark"></span>Crimson Ledge Holdings</div>
  <div class="page-no">03</div>
</section>

<!-- Table -->
<section class="slide table col-right row-3">
  <div class="works-bg"></div>
  <svg class="shapes" viewBox="0 0 750 422">
    <polygon points="592,0 750,0 750,129" fill="url(#cornerGreen)"/>
  </svg>
  <h2 class="slide-title">Our Table</h2>
  <p class="table-intro">At vero eos et accusamus et iusto odio dignissimducimus qui blanditiis praesentiuluptatum deleniti atque corrupti qus molestias excepturi sint occaecati cupiditate non provident, similique sunt in culpa qui officia deserunt mollitia animi, id est laborum et dolorum</p>
  <table class="data-table">
    <colgroup><col style="width:94px"><col style="width:93px"><col style="width:107px"><col></colgroup>
    <thead><tr><th>TITLE</th><th>DATE</th><th>STATUS</th><th>DESCRIPTION</th></tr></thead>
    <tbody>
      <tr><td>LOREM IPSUM</td><td>01/11/2025</td><td class="status">Complete</td><td>Et harum quidem rerum facilis est et expedita distinctam libero<br>temporecum solutaue corruptiue corrupti</td></tr>
      <tr><td>LOREM IPSUM</td><td>01/11/2025</td><td class="status">Complete</td><td>Et harum quidem rerum facilis est et expedita distinctam libero<br>temporecum solutaue corruptiue corrupti</td></tr>
      <tr><td>LOREM IPSUM</td><td>01/11/2025</td><td class="status">Complete</td><td>Et harum quidem rerum facilis est et expedita distinctam libero<br>temporecum solutaue corruptiue corrupti</td></tr>
      <tr><td>LOREM IPSUM</td><td>01/11/2025</td><td class="status">Complete</td><td>Et harum quidem rerum facilis est et expedita distinctam libero<br>temporecum solutaue corruptiue corrupti</td></tr>
      <tr><td>LOREM IPSUM</td><td>01/11/2025</td><td class="status">Complete</td><td>Et harum quidem rerum facilis est et expedita distinctam libero<br>temporecum solutaue corruptiue corrupti</td></tr>
    </tbody>
  </table>
  <div class="brand brand-footer"><span class="brand-mark"></span>Crimson Ledge Holdings</div>
  <div class="page-no">07</div>
</section>

<!-- Section divider -->
<section class="slide divider col-left row-4">
  <div class="divider-bg" role="img" aria-label="Abstract grey low-poly network background"></div>
  <div class="brand brand-hero"><span class="brand-mark"></span>Crimson Ledge Holdings</div>
  <h2 class="divider-heading">Section Divider Title</h2>
</section>

<!-- Thank you -->
<section class="slide thanks col-right row-4">
  <div class="thanks-bg" role="img" aria-label="Dark carbon fibre textured background"></div>
  <div class="brand brand-hero"><span class="brand-mark"></span>Crimson Ledge Holdings</div>
  <div class="thanks-rule"></div>
  <h2 class="thanks-heading">Thank You</h2>
</section>

</body>
</html>
```